Powerpoint marketing presentation

I wold like to have a powerpoint presentation with includes the attached logo for the company. I would like a background that looks good with the logo. I would like creative slides that capture the contents in an impact way. The Company's name is Velmora Services and it provides oil and gas well abandonment services. Well abandonments are often the overlooked aspect of a wells lifecycle. This is often overlooked area as it is a non-core activity to the energy company. We ensure this aspect is done in accordance with regulations and in a cost effective way. If possible I would like some creative ideas on a corporate scorecard to report results.

Target Market(s)

Oil and gas exploration and production companies

Industry/Entity Type

It Company

Font styles to use
Sans Serif

Requirements
Must have
• Presentation background incorporating logo. Creative visual capture of the business. This is a sales pitch presentation. It must be impactful.
Nice to have
• I would like to see some scorecard designs.
Should not have
• I am trying to get something that is just words on a page. Design and creativity to communicate.

```html
<!DOCTYPE html>
<html lang="en">
<head>
<meta charset="UTF-8">
<title>Velmora Services – Presentation Slides</title>
<link href="https://fonts.googleapis.com/css2?family=Open+Sans:wght@400;600;700&family=Oswald:wght@500;600&family=Arimo:wght@400;700&display=swap" rel="stylesheet">
<style>
:root{
  --green:#1e7d12;
  --green-dark:#156b0c;
  --green-bright:#5ad400;
  --canvas:#dcdcdc;
  --white:#ffffff;
  --ink:#222222;
  --muted:#555555;
  --black:#111111;
  --photo-a:#c9c6c8;
  --photo-b:#8e8a8c;
  --placeholder:#dedede;
}
*{box-sizing:border-box;margin:0;padding:0}
html,body{width:1200px;height:926px;overflow:hidden;background:var(--canvas)}
body{position:relative;font-family:"Arimo",Arial,sans-serif;color:var(--ink)}
.slide{position:absolute;width:373px;height:280px;background:var(--white);overflow:hidden}
.c1{left:24px}.c2{left:414px}.c3{left:804px}
.r1{top:24px}.r2{top:325px}.r3{top:624px}
.abs{position:absolute}

.slide-heading{position:absolute;left:20px;top:8px;font-family:"Open Sans",sans-serif;font-size:15px;color:var(--ink)}
.header-rule{position:absolute;left:20px;right:12px;top:32px;height:1px;background:#d0d0d0}
.brand{position:absolute;display:flex;align-items:center;gap:4px;font-family:"Arimo",sans-serif;font-weight:700;color:var(--black)}
.brand-dot{width:9px;height:9px;border-radius:50%;background:var(--green)}
.brand-small{right:12px;top:12px;font-size:7px}
.footer{position:absolute;left:0;bottom:0;width:373px;height:10px}

.body-text{font-size:5px;line-height:1.35;color:var(--muted)}
.title-large{font-family:"Oswald",sans-serif;font-weight:600;font-size:15px;color:var(--green);letter-spacing:.2px}

.photo{background:linear-gradient(160deg,var(--photo-a),var(--photo-b))}

.q-list{position:absolute;left:164px;top:82px}
.q-row{display:flex;align-items:center;height:25px}
.q-icon{width:20px;height:20px;border-radius:50%;background:var(--green);display:flex;align-items:center;justify-content:center;margin-right:32px}
.q-row:nth-child(2) .q-icon{margin-left:4px;margin-right:28px}
.q-row:nth-child(3) .q-icon{margin-left:6px;margin-right:26px}
.q-row:nth-child(4) .q-icon{margin-left:4px;margin-right:28px}
.q-text{font-size:8px;color:var(--ink)}

.solution{position:absolute;top:65px;width:102px;text-align:center}
.solution-disc{width:102px;height:102px;border-radius:50%;background:var(--green);color:var(--white);display:flex;flex-direction:column;align-items:center;justify-content:center;font-size:7px;line-height:1.2}
.solution-disc svg{margin-bottom:8px}
.solution-stem{margin:0 auto;width:1px;height:12px;background:var(--ink)}
.solution-node{margin:0 auto;width:7px;height:7px;border:1px solid var(--ink);border-radius:50%}
.solution .body-text{margin-top:4px}

.col-heading{font-size:8px;font-weight:700;color:var(--green);margin-bottom:5px}

.pitch-line{position:absolute;left:0;width:190px;text-align:center;color:var(--white);font-family:"Arimo",sans-serif;font-size:11px;line-height:1.3}
.benefit{position:absolute;left:230px;width:135px}
.benefit h3{font-size:7.5px;font-weight:700;color:var(--white);margin-bottom:3px}
.benefit p{font-size:4.8px;line-height:1.35;color:#e6f1e3}
.benefit-icon{position:absolute;left:188px;width:30px;height:30px;border-radius:50%;background:var(--green);border:2px solid var(--white);display:flex;align-items:center;justify-content:center}

.section-title{position:absolute;left:43px;font-size:8.5px;font-weight:700;color:var(--ink)}
.bullets{position:absolute;left:43px;list-style:none}
.bullets li{position:relative;padding-left:17px;font-size:6.5px;line-height:1.3;color:#333;margin-bottom:7px}
.bullets li::before{content:"";position:absolute;left:0;top:1px;width:6px;height:6px;border-radius:50%;background:var(--green)}
.sub{display:block}

.challenge{position:absolute;top:160px;width:80px;text-align:center;font-size:6px;line-height:1.3;color:#333}
.challenge svg{display:block;margin:0 auto 10px}

.legend{position:absolute;left:24px;width:140px}
.legend h4{font-size:8px;font-weight:700;color:var(--ink);display:flex;align-items:center;gap:8px;margin-bottom:3px}
.legend h4 span{width:7px;height:7px;border-radius:50%}
.legend p{font-size:5px;line-height:1.3;color:var(--muted);padding-left:16px}
</style>
</head>
<body>

<!-- Slide 1: title -->
<section class="slide c1 r1">
  <h1 class="abs title-large" style="left:28px;top:117px">PRESENTATION TITTLE</h1>
  <p class="abs body-text" style="left:30px;top:147px;width:150px">Lorem ipsum dolor sit amet, consectetur adipisicing elit, sed do eiusmod tempor incididunt ut labore et dolore magna aliqua. Ut enim ad minim veniam, quis nostrud exercitation ullamco laboris nisi ut</p>
  <div class="brand" style="left:30px;top:198px;font-size:11px"><span class="brand-dot" style="width:14px;height:14px"></span>Velmora Services</div>
  <div class="abs" style="left:200px;top:10px;width:330px;height:330px;border-radius:50%;background:linear-gradient(180deg,var(--green-bright),var(--green))"></div>
</section>

<!-- Slide 2: title with photo -->
<section class="slide c2 r1">
  <h1 class="abs title-large" style="left:28px;top:117px">PRESENTATION TITTLE</h1>
  <p class="abs body-text" style="left:30px;top:147px;width:150px">Lorem ipsum dolor sit amet, consectetur adipisicing elit, sed do eiusmod tempor incididunt ut labore et dolore magna aliqua. Ut enim ad minim veniam, quis nostrud exercitation ullamco laboris nisi ut</p>
  <div class="brand" style="left:30px;top:198px;font-size:11px"><span class="brand-dot" style="width:14px;height:14px"></span>Velmora Services</div>
  <div class="abs photo" role="img" aria-label="Photo of steel refinery towers and pipework" style="left:200px;top:0;width:173px;height:280px"></div>
</section>

<!-- Slide 3: questions -->
<section class="slide c3 r1">
  <h2 class="slide-heading">Heading Text</h2>
  <div class="header-rule"></div>
  <div class="brand brand-small"><span class="brand-dot"></span>Velmora Services</div>
  <div class="abs photo" role="img" aria-label="Photo of refinery towers against the sky" style="left:26px;top:78px;width:128px;height:128px;border-radius:50%"></div>
  <div class="q-list">
    <div class="q-row"><span class="q-icon"><svg width="10" height="10" viewBox="0 0 10 10"><circle cx="4" cy="4" r="2.7" fill="none" stroke="#fff" stroke-width="1.3"/><line x1="6" y1="6" x2="9" y2="9" stroke="#fff" stroke-width="1.5"/></svg></span><span class="q-text">What are your personal strengths?</span></div>
    <div class="q-row"><span class="q-icon"><svg width="10" height="10" viewBox="0 0 10 10"><path d="M5 9.5 L2 5 A3.3 3.3 0 1 1 8 5 Z" fill="#fff"/><circle cx="5" cy="3.8" r="1.2" fill="#1e7d12"/></svg></span><span class="q-text">Where is your time best spent?</span></div>
    <div class="q-row"><span class="q-icon"><svg width="10" height="10" viewBox="0 0 10 10"><circle cx="5" cy="5" r="3.6" fill="none" stroke="#fff" stroke-width="1.2"/><path d="M5 3v2.3l1.5 1" fill="none" stroke="#fff" stroke-width="1.1"/></svg></span><span class="q-text">When are you at your best?</span></div>
    <div class="q-row"><span class="q-icon"><svg width="11" height="10" viewBox="0 0 11 10"><circle cx="3.5" cy="3" r="1.6" fill="#fff"/><circle cx="7.5" cy="3" r="1.6" fill="#fff"/><path d="M0.5 8.5a3 3 0 0 1 6 0zM4.5 8.5a3 3 0 0 1 6 0z" fill="#fff"/></svg></span><span class="q-text">Who do you like to work with?</span></div>
    <div class="q-row"><span class="q-icon"><svg width="10" height="10" viewBox="0 0 10 10"><rect x="2" y="1.5" width="6" height="7.5" rx=".6" fill="none" stroke="#fff" stroke-width="1.1"/><path d="M3.5 4h3M3.5 6h2" stroke="#fff" stroke-width="1"/></svg></span><span class="q-text">Why are you in this business?</span></div>
  </div>
  <svg class="footer" viewBox="0 0 373 10"><rect width="373" height="10" fill="var(--green)"/><path d="M333 10 L343 0 H373 V10 Z" fill="#fff"/><text x="349" y="8" font-size="6" fill="#333" font-family="Arimo,sans-serif">10</text></svg>
</section>

<!-- Slide 4: three solutions -->
<section class="slide c1 r2">
  <h2 class="slide-heading">Heading Text</h2>
  <div class="header-rule"></div>
  <div class="brand brand-small"><span class="brand-dot"></span>Velmora Services</div>
  <div class="solution" style="left:25px">
    <div class="solution-disc"><svg width="22" height="24" viewBox="0 0 22 24"><circle cx="11" cy="10" r="5" fill="#fff"/><rect x="8.5" y="15" width="5" height="4" fill="#fff"/><path d="M11 1v2M3 10h2M17 10h2M5 4l1.4 1.4M17 4l-1.4 1.4" stroke="#fff" stroke-width="1.3"/></svg>OUR SOLUTION<br>ONE</div>
    <div class="solution-stem"></div><div class="solution-node"></div>
    <p class="body-text">Lorem ipsum dolor sit amet, consectetur adipisicing elit, sed do eiusmod tempor incididunt ut</p>
  </div>
  <div class="solution" style="left:135px">
    <div class="solution-disc"><svg width="22" height="24" viewBox="0 0 22 24"><rect x="3" y="3" width="16" height="19" rx="1.5" fill="none" stroke="#fff" stroke-width="1.6"/><rect x="7.5" y="1" width="7" height="4" fill="#fff"/><circle cx="11" cy="13" r="4.5" fill="none" stroke="#fff" stroke-width="1.4"/><path d="M8.8 13l1.6 1.6 3-3" fill="none" stroke="#fff" stroke-width="1.4"/></svg>OUR SOLUTION<br>TWO</div>
    <div class="solution-stem"></div><div class="solution-node"></div>
    <p class="body-text">Lorem ipsum dolor sit amet, consectetur adipisicing elit, sed do eiusmod tempor incididunt ut</p>
  </div>
  <div class="solution" style="left:245px">
    <div class="solution-disc"><svg width="22" height="24" viewBox="0 0 22 24"><circle cx="11" cy="6.5" r="5" fill="#fff"/><path d="M2 23v-4a6 6 0 0 1 6-6h6a6 6 0 0 1 6 6v4z" fill="#fff"/><path d="M11 13l-1.2 6 1.2 2 1.2-2z" fill="#1e7d12"/></svg>OUR SOLUTION<br>THREE</div>
    <div class="solution-stem"></div><div class="solution-node"></div>
    <p class="body-text">Lorem ipsum dolor sit amet, consectetur adipisicing elit, sed do eiusmod tempor incididunt ut</p>
  </div>
  <svg class="footer" viewBox="0 0 373 10"><rect width="373" height="10" fill="var(--green)"/><path d="M333 10 L343 0 H373 V10 Z" fill="#fff"/><text x="349" y="8" font-size="6" fill="#333" font-family="Arimo,sans-serif">10</text></svg>
</section>

<!-- Slide 5: two columns -->
<section class="slide c2 r2">
  <h2 class="slide-heading">Heading Text</h2>
  <div class="header-rule"></div>
  <div class="brand brand-small"><span class="brand-dot"></span>Velmora Services</div>
  <div class="abs" role="img" aria-label="Image placeholder" style="left:20px;top:48px;width:342px;height:113px;background:var(--placeholder)"></div>
  <div class="abs" style="left:20px;top:180px;width:162px">
    <h3 class="col-heading">aboris nisi ut aliquip</h3>
    <p class="body-text">Lorem ipsum dolor sit amet, consectetur adipisicing elit, sed do eiusmod tempor incididunt ut labore et dolore magna aliqua. Ut enim ad minim veniam, quis nostrud exercitation ullamco laboris nisi ut aliquip ex ea commodo. Lorem ipsum dolor sit amet, sed do eiusmod tempor incididunt ut labore et dolore magna aliqua.</p>
  </div>
  <div class="abs" style="left:192px;top:180px;width:165px">
    <h3 class="col-heading">commodo Lorem ipsum dolor</h3>
    <p class="body-text">Lorem ipsum dolor sit amet, consectetur adipisicing elit, sed do eiusmod tempor incididunt ut labore et dolore magna aliqua. Ut enim ad minim veniam, quis nostrud exercitation ullamco laboris nisi ut aliquip ex ea commodo. Lorem ipsum dolor sit amet, sed do eiusmod tempor incididunt ut labore et dolore magna aliqua.</p>
  </div>
  <svg class="footer" viewBox="0 0 373 10"><rect width="373" height="10" fill="var(--green)"/><path d="M333 10 L343 0 H373 V10 Z" fill="#fff"/><text x="349" y="8" font-size="6" fill="#333" font-family="Arimo,sans-serif">10</text></svg>
</section>

<!-- Slide 6: pitch -->
<section class="slide c3 r2" style="background:var(--black)">
  <svg class="abs" style="left:0;top:0" width="373" height="280" viewBox="0 0 373 280">
    <path d="M212 0 C180 60 180 220 200 280" fill="none" stroke="#fff" stroke-width="3"/>
    <path d="M215 0 C183 60 183 220 203 280 H373 V0 Z" fill="var(--green)"/>
  </svg>
  <p class="pitch-line" style="top:98px">WE HELP PEOPLE<br>SOLVE THEIR PROBLEM</p>
  <div class="brand" style="left:64px;top:150px;font-size:8px;color:var(--white)"><span class="brand-dot" style="background:var(--green-bright)"></span>Velmora Services</div>
  <span class="benefit-icon" style="top:77px"><svg width="12" height="12" viewBox="0 0 12 12"><circle cx="6" cy="5" r="3" fill="#fff"/><rect x="4.6" y="8" width="2.8" height="2.5" fill="#fff"/></svg></span>
  <span class="benefit-icon" style="top:117px"><svg width="12" height="12" viewBox="0 0 12 12"><path d="M1 6 L11 1 L8 11 L6 7 Z" fill="#fff"/></svg></span>
  <span class="benefit-icon" style="top:157px"><svg width="12" height="12" viewBox="0 0 12 12"><circle cx="6" cy="6" r="4.5" fill="none" stroke="#fff" stroke-width="1.2"/><circle cx="6" cy="6" r="1.8" fill="#fff"/></svg></span>
  <div class="benefit" style="top:78px"><h3>ENIM MINIM VENIAM</h3><p>Lorem ipsum dolor sit amet, consectetur adipisicing elit, sed do eiusmod tempor incididunt ut labore et dolore magna aliqua. Ut enim ad minim veniam</p></div>
  <div class="benefit" style="top:118px"><h3>ENIM MINIM VENIAM</h3><p>Lorem ipsum dolor sit amet, consectetur adipisicing elit, sed do eiusmod tempor incididunt ut labore et dolore magna aliqua. Ut enim ad minim veniam</p></div>
  <div class="benefit" style="top:158px"><h3>ENIM MINIM VENIAM</h3><p>Lorem ipsum dolor sit amet, consectetur adipisicing elit, sed do eiusmod tempor incididunt ut labore et dolore magna aliqua. Ut enim ad minim veniam</p></div>
</section>

<!-- Slide 7: bullets -->
<section class="slide c1 r3">
  <h2 class="slide-heading">Heading Text</h2>
  <div class="header-rule"></div>
  <div class="brand brand-small"><span class="brand-dot"></span>Velmora Services</div>
  <h3 class="section-title" style="top:46px">BECOME A RESOURCE FOR OTHER ADVISORS</h3>
  <ul class="bullets" style="top:64px;width:260px">
    <li>Offer to help referral sources and other advisors when they need it</li>
    <li>They will send business your way knowing you are the type of advisor that intentionally helps others</li>
  </ul>
  <h3 class="section-title" style="top:124px">LOOK BEYOND YOUR CURRENT SERVICE OFFERINGS</h3>
  <ul class="bullets" style="top:143px;width:260px">
    <li>Explore new software vendors</li>
    <li>Talk to other CPAs and understand their practices<span class="sub">• Firm Networking Groups</span></li>
    <li>See what is going on in your market (and what ISN'T going on)</li>
  </ul>
  <svg class="footer" viewBox="0 0 373 10"><rect width="373" height="10" fill="var(--green)"/><path d="M333 10 L343 0 H373 V10 Z" fill="#fff"/><text x="349" y="8" font-size="6" fill="#333" font-family="Arimo,sans-serif">10</text></svg>
</section>

<!-- Slide 8: challenges -->
<section class="slide c2 r3">
  <div class="abs photo" role="img" aria-label="Photo of industrial storage towers and pipework" style="left:0;top:0;width:373px;height:136px"></div>
  <div class="challenge" style="left:22px"><svg width="26" height="22" viewBox="0 0 26 22"><circle cx="8" cy="6" r="3.5" fill="var(--green)"/><circle cx="18" cy="6" r="3.5" fill="var(--green)"/><circle cx="13" cy="9" r="3.5" fill="var(--green)"/><path d="M1 20a7 7 0 0 1 12-5 7 7 0 0 1 12 5z" fill="var(--green)"/></svg>Shifting our clients' perception of CPAs and their value</div>
  <div class="challenge" style="left:108px"><svg width="26" height="22" viewBox="0 0 26 22"><path d="M3 8h5l11-6v18L8 14H3z" fill="var(--green)"/><path d="M22 7c2 2 2 6 0 8" fill="none" stroke="var(--green)" stroke-width="2"/></svg>Being able to say no to a prospective client</div>
  <div class="challenge" style="left:194px"><svg width="26" height="22" viewBox="0 0 26 22"><path d="M5 11a8 8 0 1 0 3-6" fill="none" stroke="var(--green)" stroke-width="2.5"/><path d="M4 2v6h6" fill="none" stroke="var(--green)" stroke-width="2.5"/><path d="M13 6v5l3 3" fill="none" stroke="var(--green)" stroke-width="2"/></svg>Finding the time to make the transition</div>
  <div class="challenge" style="left:278px"><svg width="26" height="22" viewBox="0 0 26 22"><path d="M2 7h19M16 2l5 5-5 5M24 15H5M10 10l-5 5 5 5" fill="none" stroke="var(--green)" stroke-width="2.5"/></svg>Fear of change</div>
  <div class="abs" style="left:0;bottom:0;width:373px;height:14px;background:var(--green)"></div>
</section>

<!-- Slide 9: chart -->
<section class="slide c3 r3">
  <h2 class="slide-heading">Heading Text</h2>
  <div class="header-rule"></div>
  <div class="brand brand-small"><span class="brand-dot"></span>Velmora Services</div>
  <div class="legend" style="top:50px"><h4><span style="background:var(--green)"></span>Series 1</h4><p>Oluptate velit esse cillum dolore eu fugiat nulla pariatur. Excepteur sint occaecat cupidatat non proident, sunt in culpa</p></div>
  <div class="legend" style="top:94px"><h4><span style="background:var(--black)"></span>Series 1</h4><p>Oluptate velit esse cillum dolore eu fugiat nulla pariatur. Excepteur sint occaecat cupidatat non proident, sunt in culpa</p></div>
  <div class="legend" style="top:138px"><h4 style="color:#bbb"><span style="background:#ccc"></span>Series 1</h4><p>Oluptate velit esse cillum dolore eu fugiat nulla pariatur. Excepteur sint occaecat cupidatat non proident, sunt in culpa</p></div>
  <svg class="abs" style="left:170px;top:48px" width="195" height="150" viewBox="0 0 195 150" font-family="Arimo,sans-serif" font-size="5.5" fill="#444">
    <g stroke="#e2e2e2" stroke-width=".6">
      <line x1="25" y1="10" x2="190" y2="10"/><line x1="25" y1="35" x2="190" y2="35"/><line x1="25" y1="60" x2="190" y2="60"/><line x1="25" y1="85" x2="190" y2="85"/><line x1="25" y1="110" x2="190" y2="110"/>
    </g>
    <line x1="25" y1="135" x2="190" y2="135" stroke="#999" stroke-width=".8"/>
    <g text-anchor="end"><text x="20" y="12">250</text><text x="20" y="37">200</text><text x="20" y="62">150</text><text x="20" y="87">100</text><text x="20" y="112">50</text><text x="20" y="137">0</text></g>
    <rect x="32" y="52" width="11" height="83" fill="var(--green)"/><rect x="43" y="93" width="11" height="42" fill="var(--black)"/><rect x="54" y="66" width="11" height="69" fill="#d0d0d0"/>
    <rect x="88" y="10" width="11" height="125" fill="var(--green)"/><rect x="99" y="66" width="11" height="69" fill="var(--black)"/><rect x="110" y="87" width="11" height="48" fill="#d0d0d0"/>
    <rect x="143" y="52" width="11" height="83" fill="var(--green)"/><rect x="154" y="86" width="11" height="49" fill="var(--black)"/><rect x="165" y="30" width="11" height="105" fill="#d0d0d0"/>
    <g font-weight="700" font-size="7" fill="#222" text-anchor="middle"><text x="48" y="146">2001</text><text x="104" y="146">2002</text><text x="159" y="146">2002</text></g>
  </svg>
  <svg class="footer" viewBox="0 0 373 10"><rect width="373" height="10" fill="var(--green)"/><path d="M333 10 L343 0 H373 V10 Z" fill="#fff"/><text x="349" y="8" font-size="6" fill="#333" font-family="Arimo,sans-serif">10</text></svg>
</section>

</body>
</html>
```